Q & Q Fabrications HVAC Mechanical Contractor Business Card

We need a business card for a HVAC/Plumbing Mechanical Contractor. Our website is http://www.qqfabrications-example.com. We would like to include the picture of the person on the card. Pictures of people for mock-ups can be found on our website. The blue on our logo is our primary color. We'd like this to be bold yet professional without too many colors but with some color to make sure it stands out.

Industry/Entity Type

Business

Contact Information for Business Card

Font styles to use
Sans Serif

Colors
000000

Requirements
Must have
• Our logo
• Person's picture
• Company Name
• Company Phone
• Person's email address
• Person's phone number
Nice to have
• Company Address
Should not have
• Clip art

```html
<!DOCTYPE html>
<html lang="en">
<head>
<meta charset="utf-8">
<title>Q &amp; Q Fabrications – Business Card</title>
<link rel="stylesheet" href="https://fonts.googleapis.com/css2?family=Roboto:wght@400;500&display=swap">
<style>
:root{
  --page:#d9d4cc;
  --card-black:#050505;
  --card-grey:#2a2a2a;
  --brand-blue:#3c5fa8;
  --brand-blue-light:#6f8fcf;
  --bar-blue:#3e5384;
  --gold:#cbbb9c;
  --gold-soft:#b9a98c;
  --silver:#d8d8d8;
  --rose:#c9958a;
}
*{margin:0;padding:0;box-sizing:border-box}
html,body{width:1200px;height:970px;overflow:hidden;background:var(--page)}
.card{
  position:absolute;left:50px;top:179px;width:1070px;height:595px;
  transform:scale(1.028);transform-origin:top left;
  background:radial-gradient(ellipse at 60% 45%,var(--card-black) 40%,var(--card-grey) 100%);
  font-family:"Roboto",sans-serif;overflow:hidden;
  box-shadow:0 10px 30px rgba(0,0,0,.25);
}
.card__wave{position:absolute;left:0;top:0;width:1070px;height:595px}
.brand-mark{
  position:absolute;left:135px;top:209px;width:336px;height:174px;
  display:flex;align-items:center;justify-content:center;gap:14px;
}
.brand-mark__square{width:26px;height:26px;background:var(--silver)}
.brand-mark__name{font-size:30px;font-weight:500;color:var(--silver);white-space:nowrap}
.company{position:absolute;right:77px;top:78px;text-align:right}
.company__name{font-size:41px;font-weight:500;color:var(--gold);line-height:1.1}
.company__trade{font-size:20px;color:var(--gold-soft);margin-top:4px}
.accent-bar{position:absolute;right:0;width:55px;background:var(--bar-blue)}
.accent-bar--top{top:84px;height:52px}
.accent-bar--side{top:261px;height:252px}
.person{position:absolute;right:88px;top:264px;text-align:right}
.person__name{font-size:30px;font-weight:500;color:var(--silver);line-height:1.15}
.person__role{font-size:24px;color:var(--gold)}
.contacts{position:absolute;right:78px;top:358px;list-style:none;text-align:right}
.contacts li{display:flex;align-items:center;justify-content:flex-end;gap:14px;height:29.5px;font-size:24px;color:var(--gold)}
.contacts li.contacts__address{color:var(--rose)}
.contacts svg{width:22px;height:22px;fill:none;stroke:var(--silver);stroke-width:2}
</style>
</head>
<body>
<div class="card">
  <svg class="card__wave" viewBox="0 0 1070 595">
    <defs>
      <linearGradient id="blueField" x1="0" y1="0" x2="0.6" y2="1">
        <stop offset="0" stop-color="#4c74c4"/>
        <stop offset="1" stop-color="#2f4f94"/>
      </linearGradient>
    </defs>
    <path d="M0 0H380Q300 300 420 595H0Z" fill="url(#blueField)"/>
    <path d="M380 0Q300 300 420 595" fill="none" stroke="var(--brand-blue-light)" stroke-width="10" opacity=".8"/>
  </svg>

  <div class="brand-mark">
    <span class="brand-mark__square"></span>
    <span class="brand-mark__name">Q &amp; Q Fabrications</span>
  </div>

  <div class="company">
    <div class="company__name">Q &amp; Q Fabrications, Inc.</div>
    <div class="company__trade">Mechanical Contractor</div>
  </div>
  <div class="accent-bar accent-bar--top"></div>
  <div class="accent-bar accent-bar--side"></div>

  <div class="person">
    <div class="person__name">Dana Whitlock</div>
    <div class="person__role">Head of IT Services</div>
  </div>

  <ul class="contacts">
    <li>608-555-0142 <svg viewBox="0 0 24 24"><rect x="6" y="4" width="12" height="16" rx="2"/></svg></li>
    <li>608-555-0187 <svg viewBox="0 0 24 24"><path d="M6 3l3 4-2 2a12 12 0 006 6l2-2 4 3-2 4C10 20 4 14 3 6z" fill="var(--silver)" stroke="none"/></svg></li>
    <li>www.qqfabrications-example.com <svg viewBox="0 0 24 24"><circle cx="12" cy="12" r="9"/><path d="M3 12h18M12 3c4 4 4 14 0 18M12 3c-4 4-4 14 0 18"/></svg></li>
    <li>dwhitlock@qqfabrications-example.com <svg viewBox="0 0 24 24"><rect x="4" y="7" width="16" height="11"/><path d="M4 7l8 6 8-6"/></svg></li>
    <li class="contacts__address">4170 Orchard Lane Madison,WI 53700-0000 <svg viewBox="0 0 24 24"><path d="M12 22s-6-7-6-12a6 6 0 0112 0c0 5-6 12-6 12z" fill="var(--silver)" stroke="none"/><circle cx="12" cy="10" r="2" fill="#000" stroke="none"/></svg></li>
  </ul>
</div>
</body>
</html>
```